Bifold brochure design for leadership academy

Please see below. This is a bifold brochure for a leadership academy. (www.vesk.institute). Look and feel must be colours, shapes, abstract designs, graphics, pictures. Make this professional, yet casual and bold.

Feel free to design just the front and back cover, then I'll give feedback on whether or not you're in the right direction.

COVER
- Title: “The Brightwater Year Journey”
- “Northmere Pathways Institute” logo somewhere
- Subtitles (with images, icons, and/or shapes): “Self-discovery” “Skills development” “Real-world Impact”

PAGE 2 (Inside Fold)
- Title: "The Program"
- Section 2a: Section title: "How it works”
- Image: See website, image under "four phases of the program". Please adapt and make it look better
- Text: VPI is a structured, 8-month ‘gap year’ program for 18-25 year olds who want more than just a year off – they want a year ahead. Our aim is to develop high-potential young leaders with strong values, clear purpose, high-impact skills, and a track record of real-world accomplishments that are second-to-none. We do this through four-phases.
- Section 2b: Section title: “Dates & Timing”
- Image: See image on website under 'dates and timing'. Make sure both dates show up on the brochure (September and January program).
- Text: There are two programs per year: one that starts in September, the other in January. The first four months of the program are based in Toronto at the VPI headquarters. The curriculum we work through is highly engaging and personalized, focusing directly on students’ goals. After that, students are out in the world, achieving the remaining components of the program (e.g. internship, volunteer abroad).

PAGE 3 (Outside Fold)
- Page Title: "The Students"
- Section 3a: Section title: “Who’s it for”
- Subtitle1: “High school graduates”
 Image/icon of a high school grad
 Text1: 90% of high school grads aren't sure why they’re going to university or what they want to study.
 Text2: VPI helps students discover what they truly want to do in life, and make enormous progress towards these goals.

- Subtitle2: “Post-secondary students”
 Image/icon of a university / college student
 Text1: 28% of students switch or drop out of their program because it wasn’t for them or they didn’t like it.
 Text2: Don't keep moving around or risk switching careers down the road – find out what sparks your passion with VPI.

- Subtitle3: “Post-secondary graduates”
 Image/icon of a university/ college grad
 Text1: 50% of graduates are unemployed or underemployed, 60% are in debt.
 Text2: VPI will help you get your dream job – our students won’t settle for anything less.

- Section 3b: Section title: “How to apply”
 Text1: We select high-potential young leaders with a desire to improve themselves and impact the world.
 Text2: We won’t ask you for your grades – we care more about your values and potential.
 Text3: Visit www.vesk.institute to apply now

BACK COVER
- Page Title: “Get in Touch”
- Website: www.vesk.institute
- Facebook page: facebook.com/vesk.institute
- Twitter handle: @vesk_institute
- Email: marta@vesk.institute

Target Market(s)

18-25 year olds, parents, teachers

Industry/Entity Type

Leadership

Requirements
Must have
• Beautiful design - sleek and bold, yet colourful and casual. Keep the colours similar to our website (www.vesk.institute). See examples of other brochures.
• http://img.plorvex.net/jpg/00/11/22/33/240_F_11223344_aBcDeFgHiJkLmNoPqRsTuVwXyZ123456.jpg
• http://quandrelhub.com/wp-content/uploads/2014/11/Real-Estate-Bi-fold-Brochure.jpg
• http://www.trovanic.com/media/k2/galleries/5/001-bi-fold-brochure-psd-mock-up-template.jpg
• http://img.plorvex.net/jpg/00/44/55/66/240_F_44556677_zYxWvUtSrQpOnMlKjIhGfEdCbA987654.jpg

```html
<!DOCTYPE html>
<html lang="en">
<head>
<meta charset="utf-8">
<title>VPI Brochure – The Program / The Students</title>
<link href="https://fonts.googleapis.com/css2?family=Arvo:wght@400;700&family=Crimson+Text:wght@400;600;700&family=Roboto+Condensed:wght@400;700&display=swap" rel="stylesheet">
<style>
  :root{
    --canvas:#e4e4e4;
    --paper-a:#f3f0cf;
    --paper-b:#e9e5b6;
    --red:#c3242a;
    --red-dark:#a51d22;
    --blue:#1f6fb5;
    --blue-light:#2aa3d8;
    --green:#3aa57a;
    --ink:#2b2b2b;
    --label-bg:#f7f1dc;
    --white:#ffffff;
  }
  *{box-sizing:border-box;margin:0;padding:0}
  html,body{width:1200px;height:900px;overflow:hidden}
  body{background:var(--canvas);font-family:"Crimson Text",Georgia,serif;color:var(--ink)}
  .spread{position:absolute;left:40px;top:50px;width:1120px;height:800px;display:flex;box-shadow:0 6px 24px rgba(0,0,0,.18)}
  .page{position:relative;width:560px;height:800px;background:linear-gradient(135deg,var(--paper-a),var(--paper-b));overflow:hidden}
  .page--left{border-right:1px solid rgba(0,0,0,.08)}
  .page-title{position:absolute;font-family:"Arvo",Georgia,serif;font-weight:700;font-size:24px;letter-spacing:2px;padding:6px 18px}
  .page-title--program{left:38px;top:78px;background:var(--label-bg);color:var(--red);border:2px dashed #caa;transform:rotate(-3deg)}
  .page-title--students{left:34px;top:58px;background:var(--green);color:var(--white);transform:rotate(-3deg)}
  .lead-line{position:absolute;height:2px;background:var(--blue)}
  .lead-line::before{content:"";position:absolute;left:-6px;top:-4px;width:10px;height:10px;border-radius:50%;background:var(--blue)}
  .lead-line--red{background:var(--red)}
  .lead-line--red::before{background:var(--red)}
  .section-label{position:absolute;font-family:"Arvo",Georgia,serif;font-weight:700;font-size:15px;background:var(--label-bg);border:1px dashed var(--red);padding:3px 10px;color:var(--ink)}
  .body-text{position:absolute;font-size:13.5px;line-height:1.28;text-align:justify}
  .illustration{position:absolute;border-radius:8px}
  .magnifier{left:330px;top:30px;width:170px;height:120px;background:linear-gradient(135deg,#c9c9c9,#e27a72 45%,#3f93c9);opacity:.85;border-radius:60px 60px 20px 20px}
  .phases{position:absolute;left:30px;top:300px;width:500px;height:120px;display:flex;justify-content:space-between}
  .phase{position:relative;width:110px;height:120px}
  .phase-ring{position:absolute;left:10px;top:10px;width:90px;height:90px;border-radius:50%;border:2px dotted var(--red)}
  .phase-art{position:absolute;left:30px;top:30px;width:50px;height:50px;border-radius:6px;background:linear-gradient(#3a3a3a,#8a8a8a)}
  .phase-name{position:absolute;left:-8px;top:20px;font-family:"Roboto Condensed",Arial,sans-serif;font-size:11px;transform:rotate(-60deg);transform-origin:left top;color:var(--ink)}
  .phase-tag{position:absolute;left:32px;bottom:8px;background:var(--red);color:var(--white);font-family:"Roboto Condensed",Arial,sans-serif;font-size:8px;padding:1px 6px;letter-spacing:1px}
  .calendar{position:absolute;width:120px;background:var(--white);box-shadow:0 2px 4px rgba(0,0,0,.15)}
  .calendar-head{color:var(--white);font-family:"Roboto Condensed",Arial,sans-serif;font-size:11px;text-align:center;padding:5px 0}
  .calendar--sept .calendar-head{background:var(--red)}
  .calendar--jan .calendar-head{background:var(--blue)}
  .calendar-grid{display:grid;grid-template-columns:repeat(7,1fr);gap:1px;padding:5px;font-family:"Roboto Condensed",Arial,sans-serif;font-size:6.5px;text-align:center;color:#555}
  .calendar-caption{position:absolute;font-family:"Roboto Condensed",Arial,sans-serif;font-weight:700;font-size:10px}
  .calendar-caption--red{color:var(--red)}
  .calendar-caption--blue{color:var(--blue-light)}
  .audience-bar{position:absolute;left:30px;top:182px;width:500px;height:32px;background:var(--white);display:flex;box-shadow:0 1px 3px rgba(0,0,0,.12)}
  .audience-bar span{flex:1;font-family:"Arvo",Georgia,serif;font-weight:700;font-size:11px;color:var(--blue-light);display:flex;align-items:center;justify-content:center;position:relative}
  .audience-bar span+span::before{content:"";position:absolute;left:-4px;top:4px;width:8px;height:8px;background:var(--red)}
  .divider{position:absolute;top:214px;height:80px;border-left:1px dashed var(--red)}
  .student-icon{position:absolute;top:228px;width:50px;height:60px;background:var(--red);border-radius:25px 25px 6px 6px}
  .facts{position:absolute;left:30px;top:292px;width:500px;min-height:172px;background:var(--red);display:flex;align-items:stretch;color:var(--white);font-size:12px;line-height:1.2;box-shadow:0 3px 6px rgba(0,0,0,.2)}
  .fact{flex:1;padding:10px 10px 12px;text-align:center}
  .fact+.fact{border-left:1px dashed rgba(255,255,255,.6)}
  .fact p+p{margin-top:12px}
  .steps{position:absolute;left:90px;top:548px;width:400px}
  .step{display:flex;height:36px;margin-bottom:2px;background:var(--blue);color:var(--white);font-size:12.5px}
  .step-num{width:44px;display:flex;align-items:center;justify-content:center;border-right:3px solid var(--white);font-size:14px}
  .step-text{flex:1;padding:3px 10px;line-height:1.2;display:flex;align-items:center}
</style>
</head>
<body>
<div class="spread">
  <section class="page page--left">
    <div class="lead-line" style="left:20px;top:118px;width:30px"></div>
    <h1 class="page-title page-title--program">The Program</h1>
    <div class="illustration magnifier" role="img" aria-label="Magnifying glass over stacked coloured tabs"></div>

    <div class="lead-line lead-line--red" style="left:20px;top:172px;width:40px"></div>
    <h2 class="section-label" style="left:60px;top:160px">How it works ?</h2>
    <p class="body-text" style="left:38px;top:196px;width:480px">VPI is a structured, 8-month ‘gap year’ program for 18-25 year olds who want more than just a year off – they want a year ahead. Our aim is to develop high-potential young leaders with strong values, clear purpose, high-impact skills, and a track record of real-world accomplishments that are second-to-none. We do this through four-phases.</p>

    <div class="phases">
      <div class="phase"><div class="phase-ring"></div><div class="phase-art" role="img" aria-label="Student starting the program"></div><span class="phase-name">Discover</span><span class="phase-tag">START</span></div>
      <div class="phase"><div class="phase-ring"></div><div class="phase-art" role="img" aria-label="Planning document" style="background:linear-gradient(#d9d2b8,#a99f7e)"></div><span class="phase-name">Design</span></div>
      <div class="phase"><div class="phase-ring"></div><div class="phase-art" role="img" aria-label="Presentation board with rising chart" style="background:linear-gradient(#fafafa,#d08a5a)"></div><span class="phase-name">Build</span></div>
      <div class="phase"><div class="phase-ring"></div><div class="phase-art" role="img" aria-label="Graduate celebrating at the finish" style="background:linear-gradient(#3a3a3a,#3aa57a)"></div><span class="phase-name">Accomplish</span><span class="phase-tag">FINISH</span></div>
    </div>

    <div class="lead-line lead-line--red" style="left:20px;top:488px;width:40px"></div>
    <h2 class="section-label" style="left:60px;top:476px">Dates &amp; Timing</h2>

    <div class="calendar calendar--sept" style="left:300px;top:455px">
      <div class="calendar-head">SEPTEMBER</div>
      <div class="calendar-grid">
        <span>Su</span><span>Mo</span><span>Tu</span><span>We</span><span>Th</span><span>Fr</span><span>Sa</span>
        <span></span><span></span><span>1</span><span>2</span><span>3</span><span>4</span><span>5</span>
        <span>6</span><span>7</span><span>8</span><span>9</span><span>10</span><span>11</span><span>12</span>
        <span>13</span><span>14</span><span>15</span><span>16</span><span>17</span><span>18</span><span>19</span>
        <span>20</span><span>21</span><span>22</span><span>23</span><span>24</span><span>25</span><span>26</span>
        <span>27</span><span>28</span><span>29</span><span>30</span><span></span><span></span><span></span>
      </div>
    </div>
    <div class="calendar calendar--jan" style="left:435px;top:445px">
      <div class="calendar-head">JANUARY</div>
      <div class="calendar-grid">
        <span>Su</span><span>Mo</span><span>Tu</span><span>We</span><span>Th</span><span>Fr</span><span>Sa</span>
        <span></span><span></span><span></span><span></span><span></span><span>1</span><span>2</span>
        <span>3</span><span>4</span><span>5</span><span>6</span><span>7</span><span>8</span><span>9</span>
        <span>10</span><span>11</span><span>12</span><span>13</span><span>14</span><span>15</span><span>16</span>
        <span>17</span><span>18</span><span>19</span><span>20</span><span>21</span><span>22</span><span>23</span>
        <span>24</span><span>25</span><span>26</span><span>27</span><span>28</span><span>29</span><span>30</span>
      </div>
    </div>
    <span class="calendar-caption calendar-caption--red" style="left:290px;top:572px">FULL TIME IN CLASSROOM</span>
    <span class="calendar-caption calendar-caption--blue" style="left:432px;top:562px">MONTHLY CHECKPOINTS</span>

    <p class="body-text" style="left:38px;top:640px;width:480px">There are two programs per year: one that starts in September, the other in January. The first four months of the program are based in Toronto at the VPI headquarters. The curriculum we work through is highly engaging and personalized, focusing directly on students’ goals. After that, students are out in the world, achieving the remaining components of the program (e.g. internship, volunteer abroad).</p>
  </section>

  <section class="page page--right">
    <div class="lead-line" style="left:10px;top:96px;width:24px"></div>
    <h1 class="page-title page-title--students">The Students</h1>

    <div class="lead-line lead-line--red" style="left:20px;top:150px;width:40px"></div>
    <h2 class="section-label" style="left:60px;top:138px">Who’s it for ?</h2>

    <div class="audience-bar">
      <span>High school graduates</span>
      <span>Post-secondary students</span>
      <span>Post-secondary graduates</span>
    </div>
    <div class="divider" style="left:197px"></div>
    <div class="divider" style="left:363px"></div>
    <div class="student-icon" role="img" aria-label="High school graduate icon" style="left:88px"></div>
    <div class="student-icon" role="img" aria-label="University or college student icon" style="left:255px"></div>
    <div class="student-icon" role="img" aria-label="University or college graduate icon" style="left:422px"></div>

    <div class="facts">
      <div class="fact"><p>90% of high school grads aren’t sure why they’re going to university or what they want to study.</p><p>VPI helps students discover what they truly want to do in life, and make enormous progress towards these goals.</p></div>
      <div class="fact"><p>28% of students switch or drop out of their program because it wasn’t for them or they didn’t like it.</p><p>Don’t keep moving around or risk switching careers down the road – find out what sparks your passion with VPI.</p></div>
      <div class="fact"><p>50% of graduates are unemployed or underemployed, 60% are in debt.</p><p>VPI will help you get your dream job – our students won’t settle for anything less.</p></div>
    </div>

    <div class="lead-line lead-line--red" style="left:40px;top:514px;width:40px"></div>
    <h2 class="section-label" style="left:80px;top:502px">How to Apply ?</h2>
    <div class="steps">
      <div class="step"><span class="step-num">1</span><span class="step-text">We select high-potential young leaders with a desire to improve themselves and impact the world.</span></div>
      <div class="step"><span class="step-num">2</span><span class="step-text">We won’t ask you for your grades – we care more about your values and potential.</span></div>
      <div class="step"><span class="step-num">3</span><span class="step-text">Visit www.vesk.institute to apply now</span></div>
    </div>
  </section>
</div>
</body>
</html>
```